Need a business card for a Construction and Remodeling company.
Our company logo is the fleur de lis design as thats the family crust that we use on our logos.
Heres the info it needs:

Brackmore Construction & Remodeling, LLC
Renovations * Restorations

Elwin R. Brackmore
845 North Quarry Road
Hollisford Connecticut 06488
(203) 555.0182
CT LIC/REG: 418257

home owners, customers

```html
<!DOCTYPE html>
<html lang="en">
<head>
<meta charset="utf-8">
<title>Brackmore Construction &amp; Remodeling — Business Card</title>
<link rel="stylesheet" href="https://fonts.googleapis.com/css2?family=Tinos:wght@400;700&family=Lato:wght@300;400&display=swap">
<style>
  :root {
    --page-bg: #ffffff;
    --card-bg: #30343b;
    --card-text: #ffffff;
    --card-muted: #c9ccd1;
    --rule: #e6e7ea;
  }
  * { margin: 0; padding: 0; box-sizing: border-box; }
  html, body {
    width: 847px;
    height: 1200px;
    overflow: hidden;
    background: var(--page-bg);
  }
  .canvas {
    position: relative;
    width: 847px;
    height: 1200px;
  }
  .card {
    position: absolute;
    width: 516px;
    height: 208px;
    background: var(--card-bg);
    color: var(--card-text);
    box-shadow: 0 2px 6px rgba(0, 0, 0, 0.18);
  }
  .card--front { left: 128px; top: 381px; }
  .card--back  { left: 206px; top: 607px; width: 514px; height: 212px; }

  .brand-mark {
    position: absolute;
    border: 1.5px solid var(--card-text);
    border-radius: 50%;
  }
  .card--front .brand-mark { left: 74px; top: 46px; width: 40px; height: 40px; }
  .card--back .brand-mark  { left: 432px; top: 150px; width: 34px; height: 34px; }

  .brand {
    position: absolute;
    left: 140px;
    top: 38px;
  }
  .brand__name {
    font-family: "Tinos", "Times New Roman", serif;
    font-weight: 700;
    font-size: 12.5px;
    letter-spacing: 0.3px;
    text-transform: uppercase;
    white-space: nowrap;
    padding-bottom: 5px;
    border-bottom: 1px solid var(--rule);
  }
  .brand__services {
    margin-top: 7px;
    padding-left: 3px;
    font-family: "Lato", Arial, sans-serif;
    font-weight: 300;
    font-size: 10.5px;
    color: var(--card-muted);
    white-space: nowrap;
  }

  .person {
    position: absolute;
    left: 32px;
    top: 36px;
    font-family: "Tinos", "Times New Roman", serif;
    font-weight: 700;
    font-size: 21px;
    letter-spacing: 0.2px;
  }
  .contact {
    position: absolute;
    left: 32px;
    top: 182px;
    transform: translateY(-100%);
    list-style: none;
    font-family: "Lato", Arial, sans-serif;
    font-weight: 300;
    font-size: 10.5px;
    line-height: 14.5px;
    color: var(--card-muted);
  }
</style>
</head>
<body>
<main class="canvas">
  <section class="card card--front" aria-label="Business card front">
    <span class="brand-mark" aria-hidden="true"></span>
    <div class="brand">
      <p class="brand__name">Brackmore Construction &amp; Remodeling, LLC</p>
      <p class="brand__services">Renovations &bull; Restorations</p>
    </div>
  </section>

  <section class="card card--back" aria-label="Business card back">
    <h1 class="person">Elwin R. Brackmore</h1>
    <ul class="contact">
      <li>845 North Quarry Road</li>
      <li>Hollisford Connecticut 06488</li>
      <li>(203) 555.0182</li>
      <li>CT LIC/REG: 418257</li>
    </ul>
    <span class="brand-mark" aria-hidden="true"></span>
  </section>
</main>
</body>
</html>
```